Brightline Power Crew, LLC New Business Card Design Project

Please do not submit multiple designs that look similar. Many submittals of nearly the same design will result in auto rejection. Please do not submit a design unless you know how to provide a PDF with recognizable text that I can modify and update using Adobe Acrobat. I do not use Adobe Photoshop. Please design a business card using the attached BPC logo. Be creative. Do at least 2-3 different designs. One side should have the logo large with the URL www.BPC-RT.com. The other side of the card should have the name Marcus Pellham. License number 524318. Phone number 860-555-0147. Email service@BPC-RT.com. Physical address 742 Fenwick Orchard Road, Suite 5, Harrowfield, CT. 06981. The company name should also be spelled out somewhere, Brightline Power Crew, LLC. Please ensure there is no tiny font. Please also ensure that there is nothing near the edges that might get cut off during printing. It will be 3.5" x 2" horizontal standard business card. I use CardMintly.com to order. The customer has said they want the business card to use the attached look and color scheme. Please do not submit a design unless you know how to provide a PDF with recognizable text that I can modify and update using Adobe Acrobat. I do not use Adobe Photoshop.
Target Market(s)
Read all instructions above.
Industry/Entity Type
Contact Information for Business Card
Requirements
Must have
- Read all instructions above.
Nice to have
Should not have

```html
<!DOCTYPE html>
<html lang="en">
<head>
<meta charset="utf-8">
<title>Brightline Power Crew, LLC – Business Card</title>
<link href="https://fonts.googleapis.com/css2?family=Montserrat:wght@400;500;600;700;800&display=swap" rel="stylesheet">
<style>
  :root {
    --page: #e4e4e4;
    --card: #131313;
    --card-edge: #1d1d1d;
    --gold: #f2c230;
    --gold-deep: #c9981c;
    --white: #ffffff;
    --muted: #cfcfcf;
    --ring: #d8d8d8;
  }
  * { margin: 0; padding: 0; box-sizing: border-box; }
  html, body {
    width: 1200px; height: 876px; overflow: hidden;
    background: var(--page);
    font-family: "Montserrat", Arial, sans-serif;
  }
  .sheet {
    position: relative; width: 1200px; height: 876px;
    display: flex; flex-direction: column; align-items: center; justify-content: center; gap: 28px;
  }
  .card {
    position: relative; width: 700px; height: 400px; overflow: hidden;
    background: radial-gradient(ellipse at 30% 20%, #262626 0%, var(--card) 60%, #0b0b0b 100%);
    border-radius: 4px;
    box-shadow: 0 10px 24px rgba(0,0,0,.25);
  }

  /* Front */
  .front .ring {
    position: absolute; left: 255px; top: 60px; width: 280px; height: 280px;
    border: 1.5px solid var(--ring); border-radius: 50%;
    display: flex; align-items: center; justify-content: center;
  }
  .front .mark {
    color: var(--gold); font-weight: 800; font-size: 78px; letter-spacing: 2px;
  }
  .front .url {
    position: absolute; left: 48px; bottom: 40px;
    color: var(--white); font-weight: 700; font-size: 14px; letter-spacing: 9px;
  }

  /* Back */
  .back .ring {
    position: absolute; left: 190px; top: -40px; width: 200px; height: 200px;
    border: 1.5px solid var(--ring); border-radius: 50%;
    display: flex; align-items: center; justify-content: center;
  }
  .back .mark { color: var(--gold); font-weight: 800; font-size: 46px; letter-spacing: 1px; }
  .person { position: absolute; left: 40px; top: 120px; color: var(--white); }
  .person .name { font-weight: 700; font-size: 20px; letter-spacing: .5px; }
  .person .license { font-weight: 400; font-size: 13px; margin-top: 4px; color: var(--muted); }

  .company { position: absolute; right: 40px; top: 150px; text-align: right; line-height: 1.02; }
  .company .line { display: block; font-weight: 800; font-size: 34px; color: var(--white); }
  .company .line.accent { color: var(--gold); }
  .company .line.mixed { font-size: 36px; }
  .company .url { display: block; margin-top: 12px; color: var(--white); font-weight: 600; font-size: 11px; letter-spacing: 8px; }

  .divider { position: absolute; left: 40px; right: 0; top: 282px; height: 1.5px; background: var(--gold); }

  .contact { position: absolute; left: 300px; top: 296px; color: var(--white); list-style: none; }
  .contact li { display: flex; align-items: center; gap: 8px; margin-bottom: 5px; }
  .contact svg { width: 13px; height: 13px; flex: none; }
  .contact .phone { font-weight: 700; font-size: 17px; }
  .contact .email { font-size: 12px; }
  .contact .addr { font-size: 12px; line-height: 1.35; align-items: flex-start; }

  .bar { position: absolute; left: 290px; right: 0; bottom: 0; height: 8px;
    background: linear-gradient(90deg, var(--gold-deep), var(--gold)); }
</style>
</head>
<body>
<main class="sheet">

  <section class="card front" aria-label="Card front">
    <div class="ring"><span class="mark">BPC</span></div>
    <p class="url">www.BPC-RT.com</p>
  </section>

  <section class="card back" aria-label="Card back">
    <div class="ring"><span class="mark">BPC</span></div>

    <div class="person">
      <p class="name">MARCUS PELLHAM</p>
      <p class="license">License number 524318</p>
    </div>

    <h1 class="company">
      <span class="line">BRIGHTLINE</span>
      <span class="line accent">POWER</span>
      <span class="line mixed">Crew, LLC</span>
      <span class="url">www.BPC-RT.com</span>
    </h1>

    <div class="divider"></div>

    <ul class="contact">
      <li class="phone">
        <svg viewBox="0 0 24 24" fill="none" stroke="#fff" stroke-width="2"><circle cx="12" cy="12" r="10"/><path d="M9 7l2 3-1.5 1.5a7 7 0 0 0 3 3L14 13l3 2-1 2c-4 0-9-5-9-9z"/></svg>
        860-555-0147
      </li>
      <li class="email">
        <svg viewBox="0 0 24 24" fill="none" stroke="#fff" stroke-width="2"><rect x="3" y="6" width="18" height="12" rx="1"/><path d="M3 7l9 6 9-6"/></svg>
        service@BPC-RT.com
      </li>
      <li class="addr">
        <svg viewBox="0 0 24 24" fill="none" stroke="#fff" stroke-width="2"><path d="M12 22s7-7 7-12a7 7 0 0 0-14 0c0 5 7 12 7 12z"/><circle cx="12" cy="10" r="2.5"/></svg>
        <span>742 Fenwick Orchard Road, Suite 5, Harrowfield,<br>CT 06981</span>
      </li>
    </ul>

    <div class="bar"></div>
  </section>

</main>
</body>
</html>
```